Maple Glow Label

Design a label for new brand called Maple Glow. The specific product label :
Maple Glow Cocoa Butter Lotion. You only need to design the front label.
I have included the logo and a bottle jpeg with 2 bottles on it. Please try your best.

Requirements
Must have
• text on the label other than the logo:
cocoa butter
lotion
8.5oz/250ml

Original Moisturizing Formula
Smoothes Marks
Protect Skin

__________________________________
- ALTERNATIVE TEXT TO ALSO USE:
Smoothes Dry Skin, Blemishes & Stretch Marks
Softens Hands, Face and Body
Vitamin E

```html
<!DOCTYPE html>
<html lang="en">
<head>
<meta charset="utf-8">
<title>Maple Glow Cocoa Butter Lotion – Front Labels</title>
<link rel="stylesheet" href="https://fonts.googleapis.com/css2?family=Oswald:wght@400;500&family=Questrial&display=swap">
<style>
  :root {
    --canvas-bg: #efe9e3;
    --cream-top: #ffffff;
    --cream-bottom: #f5cfae;
    --cocoa-ink: #3b2320;
    --olive-brand: #4a5a2a;
    --rule-olive: #4f5a33;
    --pod-brown: #8a5a44;
    --pod-light: #d8c3b5;
    --blush: #f5bfb2;
    --rose-brand: #e0206e;
    --rose-rule: #d8306e;
    --pod-red: #b4573a;
    --leaf-green: #5f8a3c;
    --dark-text: #3a2a28;
  }
  * { margin: 0; padding: 0; box-sizing: border-box; }
  html, body { width: 1200px; height: 1000px; overflow: hidden; }
  body {
    background: var(--canvas-bg);
    position: relative;
  }

  .label {
    position: absolute;
    display: flex;
    flex-direction: column;
    align-items: center;
    text-align: center;
    overflow: hidden;
  }

  /* Cream pump-bottle label */
  .label--cream {
    left: 242px; top: 355px;
    width: 260px; height: 505px;
    border-radius: 50% 50% 14px 14px / 26% 26% 14px 14px;
    background: linear-gradient(to bottom, var(--cream-top) 0%, var(--cream-top) 30%, var(--cream-bottom) 100%);
    font-family: "Oswald", sans-serif;
    color: var(--cocoa-ink);
  }
  .label--cream .pod-art {
    margin-top: 28px;
    width: 130px; height: 118px;
    border-radius: 50%;
    background: radial-gradient(circle, var(--pod-light) 0%, var(--pod-brown) 100%);
  }
  .label--cream .product-name {
    margin-top: 40px;
    font-weight: 500;
    font-size: 33px;
    line-height: 38px;
    letter-spacing: 1.5px;
    text-transform: uppercase;
  }
  .label--cream .brand-name {
    margin-top: 30px;
    font-weight: 500;
    font-size: 40px;
    line-height: 46px;
    color: var(--olive-brand);
  }
  .label--cream .claims {
    margin-top: 34px;
    font-size: 13px;
    line-height: 17px;
    font-variant: small-caps;
    letter-spacing: 0.5px;
  }
  .label--cream .rule {
    width: 200px; height: 1px;
    margin-top: 8px;
    background: var(--rule-olive);
  }
  .label--cream .volume {
    margin-top: 12px;
    font-size: 13px;
    font-variant: small-caps;
    letter-spacing: 0.5px;
  }

  /* Blush flip-cap bottle label */
  .label--blush {
    left: 655px; top: 330px;
    width: 345px; height: 485px;
    border-radius: 50% 50% 34px 34px / 40% 40% 30px 30px;
    background: var(--blush);
    font-family: "Questrial", sans-serif;
    color: var(--dark-text);
  }
  .label--blush .pod-art {
    margin-top: 24px;
    width: 150px; height: 118px;
    border-radius: 40% 40% 50% 50%;
    background: linear-gradient(135deg, var(--leaf-green) 0%, var(--pod-red) 55%, #e8b59e 100%);
  }
  .label--blush .product-name {
    margin-top: 24px;
    font-size: 35px;
    line-height: 40px;
    letter-spacing: 0.5px;
  }
  .label--blush .brand-name {
    margin-top: 30px;
    font-size: 46px;
    line-height: 52px;
    color: var(--rose-brand);
  }
  .label--blush .claims {
    margin-top: 26px;
    font-size: 17px;
    line-height: 20px;
  }
  .label--blush .rule {
    width: 200px; height: 2px;
    margin-top: 8px;
    background: var(--rose-rule);
  }
  .label--blush .volume {
    margin-top: 10px;
    font-size: 13px;
  }
</style>
</head>
<body>
  <section class="label label--cream" aria-label="Maple Glow cocoa butter lotion label, cream version">
    <div class="pod-art" role="img" aria-label="Line illustration of two open cocoa pods inside a brush circle"></div>
    <h1 class="product-name">Cocoa Butter<br>Lotion</h1>
    <p class="brand-name">Maple Glow</p>
    <p class="claims">Original Moisturizing Formula<br>Smoothes Marks<br>Protect Skin</p>
    <div class="rule"></div>
    <p class="volume">8.5oz/250ml</p>
  </section>

  <section class="label label--blush" aria-label="Maple Glow cocoa butter lotion label, blush version">
    <div class="pod-art" role="img" aria-label="Colour illustration of a whole and a halved cocoa pod with green leaves"></div>
    <h2 class="product-name">cocoa butter<br>lotion</h2>
    <p class="brand-name">Maple Glow</p>
    <p class="claims">Original Moisturizing Formula<br>Smoothes Marks<br>Protect Skin</p>
    <div class="rule"></div>
    <p class="volume">8.5oz/250ml</p>
  </section>
</body>
</html>
```